Quarveling stickers design for our main topics (for example: agile and Kanban)

We are looking for sticker design, that will reflect our cooperate identity and can be used for the different topics in our company. We would like to start with our Agile Coaching Offers with a Kanban Sticker saying "stop starting, start finishing", A bad example can be find in the file upload ;)
Check out our homepage to get a feeling for the cooperate identity (www.quarveling.ch)

Target Market(s)

Customers and trainees from our trainings

Industry/Entity Type

Consulting

Colors
0355a3
fbed22

Requirements
Must have
• a cool design thats fits to our customer design
the 2 lines can be changed for future stickers ... like in the example "stop starting, start finishing" and "we show you how"
Nice to have
• -
Should not have
• -

```html
<!DOCTYPE html>
<html lang="en">
<head>
<meta charset="utf-8">
<title>Quarveling stickers – Stop starting, start finishing</title>
<link rel="stylesheet" href="https://fonts.googleapis.com/css2?family=Jost:ital,wght@0,500;1,600&family=Barlow+Semi+Condensed:wght@300;400;700&display=swap">
<style>
  :root {
    --canvas: #e6e6e6;
    --ink: #000000;
    --paper: #ffffff;
    --signal: #fbe81e;
    --soft-shadow: #b3b3b3;
  }
  * { box-sizing: border-box; margin: 0; padding: 0; }
  html, body { width: 884px; height: 1200px; overflow: hidden; }
  body { background: var(--canvas); position: relative; color: var(--ink); }

  .sticker {
    position: absolute;
    width: 368px;
    height: 147px;
    background: var(--paper);
    display: flex;
    flex-direction: column;
    align-items: center;
    justify-content: center;
    text-align: center;
  }
  .col-left { left: 54px; }
  .col-right { left: 463px; }
  .row-1 { top: 87px; }
  .row-2 { top: 267px; }
  .row-3 { top: 448px; }
  .row-4 { top: 634px; }
  .row-5 { top: 815px; }

  .rounded { border-radius: 20px; }
  .dark { background: var(--ink); color: var(--paper); }
  .outlined { border: 4.5px solid var(--ink); }
  .shadow-soft { box-shadow: 9px 9px 0 var(--soft-shadow); }
  .shadow-hard { box-shadow: 10px 10px 0 var(--ink); }

  .script-line {
    font-family: "Jost", sans-serif;
    font-size: 35px;
    line-height: 40px;
  }
  .script-line--plain { font-weight: 500; letter-spacing: 0.5px; }
  .script-line--accent { font-weight: 600; font-style: italic; letter-spacing: 0.6px; }
  .script-line--signal { color: var(--signal); }

  .caps-line {
    font-family: "Barlow Semi Condensed", sans-serif;
    font-size: 29px;
    line-height: 27px;
    text-transform: uppercase;
    letter-spacing: 0.6px;
  }
  .caps-line--bold { font-weight: 700; }
  .caps-line--light { font-weight: 300; }
  .caps-line--large { font-size: 30px; line-height: 33px; font-weight: 400; }
  .highlight { background: var(--signal); padding: 0 8px 0 12px; }

  .web-address {
    font-family: "Barlow Semi Condensed", sans-serif;
    font-weight: 700;
    font-size: 12.5px;
    letter-spacing: 0.4px;
    text-transform: uppercase;
    margin-top: 9px;
  }
  .web-address--light { font-weight: 400; margin-top: 4px; }

  .ruled::before, .ruled::after {
    content: "";
    position: absolute;
    left: 29px;
    right: 28px;
    height: 3px;
    background: var(--ink);
  }
  .ruled::before { top: 17px; }
  .ruled::after { bottom: 17px; }

  .outline-set { position: absolute; left: 0; top: 1028px; }
  .outline-set text {
    font-family: "Barlow Semi Condensed", sans-serif;
    font-weight: 700;
    font-size: 31px;
    text-anchor: middle;
    letter-spacing: 0.4px;
    stroke: var(--ink);
    stroke-width: 7px;
    stroke-linejoin: round;
    paint-order: stroke;
  }
  .outline-set .fill-signal { fill: var(--signal); }
  .outline-set .fill-paper { fill: var(--paper); }
</style>
</head>
<body>
  <div class="sticker rounded col-left row-1">
    <p class="script-line script-line--plain">Stop starting</p>
    <p class="script-line script-line--accent">Start finishing</p>
  </div>
  <div class="sticker rounded dark col-right row-1">
    <p class="script-line script-line--plain">Stop starting</p>
    <p class="script-line script-line--accent">Start finishing</p>
  </div>

  <div class="sticker rounded outlined col-left row-2">
    <p class="script-line script-line--plain">Stop starting</p>
    <p class="script-line script-line--accent">Start finishing</p>
  </div>
  <div class="sticker rounded dark shadow-soft col-right row-2">
    <p class="script-line script-line--plain">Stop starting</p>
    <p class="script-line script-line--accent script-line--signal">Start finishing</p>
  </div>

  <div class="sticker rounded shadow-hard col-left row-3">
    <p class="script-line script-line--plain">Stop starting</p>
    <p class="script-line script-line--accent">Start finishing</p>
  </div>
  <div class="sticker shadow-hard col-right row-3" style="top:446px">
    <p class="caps-line caps-line--bold">Stop starting,</p>
    <p class="caps-line caps-line--bold">Start finishing.</p>
    <p class="web-address">www.quarveling.ch</p>
  </div>

  <div class="sticker col-left row-4">
    <p class="caps-line caps-line--light">Stop starting,</p>
    <p class="caps-line caps-line--bold">Start finishing.</p>
    <p class="web-address">www.quarveling.ch</p>
  </div>
  <div class="sticker outlined col-right row-4">
    <p class="caps-line caps-line--light">Stop starting,</p>
    <p class="caps-line caps-line--bold">Start finishing.</p>
    <p class="web-address">www.quarveling.ch</p>
  </div>

  <div class="sticker outlined col-left row-5">
    <p class="caps-line caps-line--large">Stop starting,</p>
    <p class="caps-line caps-line--large"><span class="highlight">Start finishing.</span></p>
    <p class="web-address web-address--light">www.quarveling.ch</p>
  </div>
  <div class="sticker ruled col-right row-5">
    <p class="caps-line caps-line--large">Stop starting,</p>
    <p class="caps-line caps-line--large"><span class="highlight">Start finishing.</span></p>
    <p class="web-address web-address--light">www.quarveling.ch</p>
  </div>

  <svg class="outline-set" width="884" height="90" viewBox="0 0 884 90" aria-label="Outlined die-cut lettering">
    <text class="fill-signal" x="239" y="35">STOP STARTING,</text>
    <text class="fill-signal" x="239" y="68">START FINISHING.</text>
    <text class="fill-paper" x="648" y="35">STOP STARTING,</text>
    <text class="fill-paper" x="648" y="68">START FINISHING.</text>
  </svg>
</body>
</html>
```